Recruitment technology firm needs a downloadable pdf to generate leads.

We need design work for a downloadable pdf that will serve as an educational document to visitors to our website. We help clients identify candidates that fit their job posting. We do that by defining the personality of the job and then assessing the personality of the candidates. We then mathematically compare and rank all the candidates against the job. Our colour scheme is blue. The final design should move from communicating a lack of fit or frustration to people fitting their job and success per the text we have built. People who download this lead generator will be added to our email list for re-marketing purposes. our website is www.brindlewaveadvisory.com. I've attached an example of a lead generator (ebike)for a business unrelated to ours.

Target Market(s)

Our target market is businesses of 50-300 people, we're targeting business owners or executives of entrepreneurial (vs. corporate) companies.

Colors
85acd3
3377b5
0455a3

Requirements
Must have
• Easy to read so text isn't overwhelming.
Nice to have
• Don't be compelled to use our website photos or those like it. I'd like this to reflect entrepreneurial companies, not corporate, suit and tie companies.

```html
<!DOCTYPE html>
<html lang="en">
<head>
<meta charset="utf-8">
<title>5 Reasons You Suck at Hiring for Fit</title>
<link rel="stylesheet" href="https://fonts.googleapis.com/css2?family=Anton&family=Montserrat:wght@600&family=Open+Sans:wght@400;600;700&display=swap">
<style>
  :root {
    --navy: #0455a3;
    --deep: #0a4f8c;
    --mid: #3377b5;
    --sky: #85acd3;
    --cyan: #2bbbe6;
    --cyan-light: #35c3ec;
    --ink: #222a33;
    --grid: #9aa3ab;
    --job: #e3001b;
    --paper: #ffffff;
    --bg: #dcdcdc;
  }
  * { margin: 0; padding: 0; box-sizing: border-box; }
  html, body { width: 714px; height: 1200px; overflow: hidden; background: var(--bg); }

  .sheet {
    position: absolute; left: 150px; width: 707px; height: 1000px;
    transform: scale(0.585); transform-origin: top left;
    background: var(--paper); overflow: hidden;
    font-family: "Open Sans", Arial, sans-serif; color: var(--ink);
    box-shadow: 0 4px 14px rgba(0,0,0,.25);
  }
  .sheet-reasons { top: 8px; }
  .sheet-solution { top: 607px; }

  /* shared */
  .photo { position: absolute; }
  .title {
    position: absolute; text-align: right; color: #fff; text-transform: uppercase;
    font-family: "Anton", Impact, sans-serif; font-weight: 400;
  }
  .body { font-size: 8.6px; line-height: 1.32; }
  .badge {
    flex: none; width: 13px; height: 13px; border-radius: 50%; background: var(--mid); color: #fff;
    font-size: 8px; font-weight: 700; display: flex; align-items: center; justify-content: center;
  }
  .reason { margin-top: 12px; }
  .reason h3 { display: flex; gap: 6px; align-items: flex-start; font-size: 8.6px; font-weight: 700; line-height: 1.3; margin-bottom: 4px; }
  .reason .body { padding-left: 19px; }

  .footer {
    position: absolute; left: 60px; right: 44px; top: 950px; display: flex; justify-content: space-between; align-items: center;
    font-size: 7px; font-weight: 700; line-height: 1.25; color: var(--ink);
  }
  .contact { display: flex; align-items: center; gap: 8px; }
  .contact svg { width: 24px; height: 24px; flex: none; }
  .contact .link { color: var(--cyan); }

  /* page one */
  .brand {
    position: absolute; left: 36px; top: 42px; display: flex; align-items: center; gap: 9px;
    font-family: "Montserrat", Arial, sans-serif; font-weight: 600; font-size: 25px; letter-spacing: 1.5px; color: #4a5560;
  }
  .brand-dot { width: 20px; height: 20px; border-radius: 50%; background: var(--navy); }
  .sheet-reasons .photo {
    left: 0; top: 120px; width: 707px; height: 368px;
    background: linear-gradient(115deg, #e4ebf1 0%, #c8d3dc 35%, #8f9eac 62%, #5c6d7e 100%);
  }
  .sheet-reasons .title-band {
    position: absolute; left: 355px; top: 0; width: 317px; height: 488px;
    background: linear-gradient(180deg, #0e75bd 0%, #0a5d9f 25%, rgba(8,80,140,.93) 100%);
  }
  .sheet-reasons .title { right: 63px; top: 52px; font-size: 68px; line-height: 1.03; }
  .sheet-reasons .title .num { display: block; font-size: 112px; line-height: 1; margin-bottom: 4px; }

  .intro { position: absolute; left: 36px; top: 512px; width: 283px; }
  .intro h2 { font-size: 15.5px; font-weight: 700; line-height: 1.18; margin-bottom: 12px; }
  .lead { font-size: 8.6px; font-weight: 700; margin-bottom: 5px; }

  .reason-panel {
    position: absolute; left: 355px; top: 488px; width: 317px; height: 440px;
    background: var(--cyan-light); color: #fff; padding: 20px 22px 0 24px;
  }
  .reason-panel .reason:first-child { margin-top: 0; }
  .reason-panel .badge { background: #fff; color: var(--cyan); }

  /* page two */
  .sheet-solution .photo {
    left: 0; top: 64px; width: 707px; height: 358px;
    background: linear-gradient(110deg, #c9ccd0 0%, #a7adb4 30%, #6c7885 60%, #3f4c5c 100%);
  }
  .sheet-solution .title-band {
    position: absolute; left: 353px; top: 0; width: 318px; height: 422px;
    background: linear-gradient(180deg, var(--cyan) 0, var(--cyan) 64px, rgba(4,70,140,.94) 64px, rgba(8,60,120,.92) 100%);
  }
  .sheet-solution .title { right: 66px; top: 78px; font-size: 80px; line-height: 1.04; }

  .solution-text { position: absolute; left: 36px; top: 440px; width: 283px; font-size: 8.2px; line-height: 1.22; }
  .solution-text p { margin-bottom: 9px; }
  .solution-panel {
    position: absolute; left: 353px; top: 422px; width: 318px; height: 180px;
    background: var(--cyan-light); color: #fff; padding: 18px 22px 0 22px; font-size: 8.2px; line-height: 1.22;
  }
  .solution-panel p { margin-bottom: 9px; }
  .fit-chart { position: absolute; left: 0; top: 0; width: 707px; height: 1000px; font-family: "Open Sans", Arial, sans-serif; }
  .fit-chart .label { font-size: 7.2px; font-weight: 700; fill: #fff; text-transform: uppercase; }
  .fit-chart .tick { font-size: 7.5px; fill: var(--ink); text-anchor: middle; }
</style>
</head>
<body>

<!-- Page one: the problem -->
<article class="sheet sheet-reasons">
  <div class="photo" role="img" aria-label="Photo of colleagues meeting in a bright office, a smiling woman in glasses in the foreground"></div>
  <div class="brand"><span class="brand-dot"></span>BRINDLEWAVE</div>
  <div class="title-band">
    <h1 class="title"><span class="num">5</span>Reasons<br>you suck<br>at hiring<br>for fit.</h1>
  </div>

  <section class="intro">
    <h2>Hiring the wrong fit is painful,<br>we are with you there.</h2>
    <p class="lead">Bad hires ruin your day, every day.</p>
    <p class="body">You want to make sure your next hire is the right one. You know what it’s like when you hire the wrong person – they aren’t productive, they don’t get along with others, there’s tension, you have to let them go, and you re-start the whole process over again.</p>
    <div class="reason">
      <h3><span class="badge">1</span>You have not defined the obstacles found in the job.</h3>
      <p class="body">Every job has its challenges and you need to find someone who will deal with the challenges as a high performer would. Spending too much time in unstructured conversation or putting too much emphasis on selling the role can detract from this key insight. Define the top 2-5 obstacles and learn how the candidate has or would tackle them.</p>
    </div>
    <div class="reason">
      <h3><span class="badge">2</span>You describe the job using words, not data.</h3>
      <p class="body">Detail oriented means different things to different people. You only find out after you have hired someone that they are not detailed enough (or are too detailed!). The same can happen when we say a candidate needs to be proactive or risk oriented. You only find out later that you hired too much or too little. You used words and not numbers to define what you needed for the role.</p>
    </div>
  </section>

  <section class="reason-panel">
    <div class="reason">
      <h3><span class="badge">3</span>You assume knowledge and experience equals performance.</h3>
      <p class="body">Just because someone’s resume says they are a strong manager does not mean they are one. And yet this is how you screen and rank your candidates. The best resumes rise to the top. But resumes are a terrible predictor of performance. Success at one company does not mean success in yours. Who are you overlooking that may be a better performer? (we have an idea below)</p>
    </div>
    <div class="reason">
      <h3><span class="badge">4</span>You are biased and subjective in your assessment of others.</h3>
      <p class="body">You get attracted to certain resumes and backgrounds. You make judgement calls on phone interviews. You do the same when you meet someone and during an interview. Very few recruitment processes have a way of OBJECTIVELY ranking and comparing candidates. As a result we end up picking someone we like as opposed to someone who will excel in the job.</p>
    </div>
    <div class="reason">
      <h3><span class="badge">5</span>You think your “gut” makes good decisions.</h3>
      <p class="body">a. “Gut” has more to do with how likeable someone is than how effective they will be. Effectiveness comes from a person’s ability to consistently behave in a manner that produces exceptional results. Do not make judgement calls on behaviours a candidate shows but may not be able to consistently repeat.</p>
    </div>
  </section>

  <footer class="footer">
    <div class="contact">
      <svg viewBox="0 0 26 26" aria-hidden="true"><circle cx="13" cy="13" r="13" fill="var(--navy)"/><path d="M9 7.5l2.2-.5 1.2 3-1.4 1a7 7 0 0 0 3.4 3.4l1-1.4 3 1.2-.5 2.2c-5 .6-9.5-3.9-8.9-8.9z" fill="#fff"/></svg>
      <span>PHONE: 555-014-2290<br>TOLL FREE: 1-800-555-0177</span>
    </div>
    <div class="contact">
      <svg viewBox="0 0 26 26" aria-hidden="true"><circle cx="13" cy="13" r="13" fill="var(--navy)"/><rect x="7" y="9" width="12" height="8.5" fill="none" stroke="#fff" stroke-width="1.3"/><path d="M7 9l6 5 6-5" fill="none" stroke="#fff" stroke-width="1.3"/></svg>
      <span>email@<span class="link">brindlewaveadvisory</span>.com</span>
    </div>
    <div class="contact">
      <svg viewBox="0 0 26 26" aria-hidden="true"><circle cx="13" cy="13" r="13" fill="var(--navy)"/><rect x="8" y="10" width="5" height="9" fill="none" stroke="#fff" stroke-width="1.2"/><rect x="13" y="7" width="5" height="12" fill="none" stroke="#fff" stroke-width="1.2"/></svg>
      <span>#212, 48 LARKSPUR LANE<br>FAIRHAVEN, ALBERTA,<br>CANADA T0X 1Z9</span>
    </div>
  </footer>
</article>

<!-- Page two: the solution -->
<article class="sheet sheet-solution">
  <div class="photo" role="img" aria-label="Photo of a team shaking hands and smiling in a casual office"></div>
  <div class="title-band">
    <h2 class="title">So how<br>can you<br>hire<br>for fit?</h2>
  </div>

  <section class="solution-text">
    <p>Personality is the most significant predictor of both fit to the manager and performance in the role. It is also one of the most difficult things to assess without the use of an objective tool.</p>
    <p>Most candidates behave a certain way in an interview, but it may be something that is difficult for them to sustain.</p>
    <p>To start addressing the problem of hiring bad fits you need to add more objectivity to your process. FitLens is a tool designed to define a benchmark of what personality is required in a role using data. Everyone gets on the same page of what success looks like.</p>
  </section>

  <section class="solution-panel">
    <p>From there each candidate completes a Persona.scan personality survey within the FitLens tool. Then they are compared equally to the benchmark and ranked objectively. All candidates are compared using the same personality dimensions.</p>
    <p>You leverage specific data and our insight to find the best candidates … Your ability to consistently hire above average fits increases … You achieve more.</p>
    <p>Here are the results of a candidate compared to a job. The job is represented in red, the candidate is represented in black.</p>
  </section>

  <svg class="fit-chart" viewBox="0 0 707 1000" role="img" aria-label="Chart comparing a candidate's personality scores with the job benchmark">
    <rect x="36" y="620" width="635" height="306" fill="none" stroke="#c5cbd0" stroke-width="1"/>
    <!-- upper dimensions -->
    <g fill="var(--mid)">
      <rect x="36" y="620" width="108" height="35"/><rect x="36" y="656" width="108" height="35"/>
      <rect x="36" y="692" width="108" height="35"/><rect x="36" y="728" width="108" height="36"/>
    </g>
    <text class="label" x="44" y="641">Assertiveness</text>
    <text class="label" x="44" y="677">Sociability</text>
    <text class="label" x="44" y="713">Pace</text>
    <text class="label" x="44" y="744">Detail</text>
    <text class="label" x="44" y="753">Orientation</text>
    <g stroke="var(--grid)" stroke-width="1">
      <line x1="144" y1="620" x2="671" y2="620"/><line x1="144" y1="655.5" x2="671" y2="655.5"/>
      <line x1="144" y1="691.5" x2="671" y2="691.5"/><line x1="144" y1="727.5" x2="671" y2="727.5"/>
      <line x1="36" y1="764" x2="671" y2="764"/>
    </g>
    <line x1="431" y1="620" x2="431" y2="764" stroke="var(--grid)" stroke-dasharray="3 3"/>
    <g>
      <text class="tick" x="169" y="783">-5</text><text class="tick" x="221" y="783">-4</text>
      <text class="tick" x="274" y="783">-3</text><text class="tick" x="326" y="783">-2</text>
      <text class="tick" x="379" y="783">-1</text><text class="tick" x="431" y="783">0</text>
      <text class="tick" x="483" y="783">1</text><text class="tick" x="536" y="783">2</text>
      <text class="tick" x="588" y="783">3</text><text class="tick" x="641" y="783">4</text>
    </g>
    <line x1="36" y1="791" x2="671" y2="791" stroke="var(--grid)"/>
    <polyline points="513,636 482,676 325,710 412,749" fill="none" stroke="var(--job)" stroke-width="1.4" stroke-dasharray="3 2"/>
    <g fill="var(--job)">
      <rect x="509" y="632" width="8" height="8"/><rect x="478" y="672" width="8" height="8"/>
      <rect x="321" y="706" width="8" height="8"/><rect x="408" y="745" width="8" height="8"/>
    </g>
    <polyline points="528,636 406,668 379,710 425,749" fill="none" stroke="#111" stroke-width="1.4"/>
    <g fill="#111">
      <circle cx="528" cy="636" r="4"/><circle cx="406" cy="668" r="4"/>
      <circle cx="379" cy="710" r="4"/><circle cx="425" cy="749" r="4"/>
    </g>
    <!-- lower dimensions -->
    <g fill="var(--sky)">
      <rect x="36" y="792" width="108" height="35"/><rect x="36" y="828" width="108" height="35"/>
      <rect x="36" y="864" width="108" height="36"/>
    </g>
    <text class="label" x="44" y="807">Behavioral</text>
    <text class="label" x="44" y="816">Adaptability</text>
    <text class="label" x="44" y="849">Emotiveness</text>
    <text class="label" x="44" y="885">Creativity</text>
    <g stroke="var(--grid)" stroke-width="1">
      <line x1="144" y1="827.5" x2="671" y2="827.5"/><line x1="144" y1="863.5" x2="671" y2="863.5"/>
      <line x1="36" y1="900" x2="671" y2="900"/>
    </g>
    <g>
      <text class="tick" x="169" y="918">0</text><text class="tick" x="221" y="918">1</text>
      <text class="tick" x="274" y="918">2</text><text class="tick" x="326" y="918">3</text>
      <text class="tick" x="379" y="918">4</text><text class="tick" x="431" y="918">5</text>
      <text class="tick" x="483" y="918">6</text><text class="tick" x="536" y="918">7</text>
      <text class="tick" x="588" y="918">8</text><text class="tick" x="641" y="918">9</text>
    </g>
    <g fill="var(--job)">
      <rect x="479" y="806" width="8" height="8"/><rect x="479" y="842" width="8" height="8"/><rect x="479" y="878" width="8" height="8"/>
    </g>
    <g fill="#111">
      <circle cx="572" cy="810" r="4"/><circle cx="645" cy="846" r="4"/><circle cx="502" cy="882" r="4"/>
    </g>
  </svg>

  <footer class="footer">
    <div class="contact">
      <svg viewBox="0 0 26 26" aria-hidden="true"><circle cx="13" cy="13" r="13" fill="var(--navy)"/><path d="M9 7.5l2.2-.5 1.2 3-1.4 1a7 7 0 0 0 3.4 3.4l1-1.4 3 1.2-.5 2.2c-5 .6-9.5-3.9-8.9-8.9z" fill="#fff"/></svg>
      <span>PHONE: 555-014-2290<br>TOLL FREE: 1-800-555-0177</span>
    </div>
    <div class="contact">
      <svg viewBox="0 0 26 26" aria-hidden="true"><circle cx="13" cy="13" r="13" fill="var(--navy)"/><rect x="7" y="9" width="12" height="8.5" fill="none" stroke="#fff" stroke-width="1.3"/><path d="M7 9l6 5 6-5" fill="none" stroke="#fff" stroke-width="1.3"/></svg>
      <span>email@<span class="link">brindlewaveadvisory</span>.com</span>
    </div>
    <div class="contact">
      <svg viewBox="0 0 26 26" aria-hidden="true"><circle cx="13" cy="13" r="13" fill="var(--navy)"/><rect x="8" y="10" width="5" height="9" fill="none" stroke="#fff" stroke-width="1.2"/><rect x="13" y="7" width="5" height="12" fill="none" stroke="#fff" stroke-width="1.2"/></svg>
      <span>#212, 48 LARKSPUR LANE<br>FAIRHAVEN, ALBERTA,<br>CANADA T0X 1Z9</span>
    </div>
  </footer>
</article>

</body>
</html>
```